i would like a business card to leave with customers and potential customers for electrical work and for the supply and install of reverse cycle airconditioning in the domestic and commercial market.
I own my own business and im a sole trader. I have an a'class electrical lisence and also a refrigeration lisence so i am
able to offer complete installations in airconditioning by a fully qualified and lisenced tradesman.
im looking for something that comes across as unique and professional.
i had the coluor black and some gold in mind but open to any coluors.
something like Brightline Electrical & Refrigeration
or Brightline Air.
i will use this design on a business card to advertise through summer to help generate installs through the busy season.

Target Market(s)

Mainly domestic house holds through summer who are in need of airconditioning and reliable information to acomadate thier cooling and heating requirements

Industry/Entity Type

Electrical

Requirements
Must have
• Business name- Brightline
My name- Peter Mulvane
My mobile no- 0438 517 209
My email- rtmulvane@kestrelnet.com.au
Installation & Decomissioning of aiconditioning split systems
LIC NO: TKR 504613
Nice to have
• Brightline Electrical & Refrigeration

```html
<!DOCTYPE html>
<html lang="en">
<head>
<meta charset="utf-8">
<title>Brightline Electrical &amp; Refrigeration – Business Card</title>
<link href="https://fonts.googleapis.com/css2?family=Arimo:wght@400&family=Tinos:wght@400&display=swap" rel="stylesheet">
<style>
  :root {
    --page: #ffffff;
    --card-dark: #000000;
    --card-light: #ffffff;
    --gold: #fbb80f;
    --cyan: #1fb5e8;
    --ink: #111111;
    --paper-edge: #b8b8b8;
    --on-dark: #ffffff;
  }
  * { margin: 0; padding: 0; box-sizing: border-box; }
  html, body {
    width: 1200px; height: 900px; overflow: hidden;
    background: var(--page);
  }
  .canvas { position: relative; width: 1200px; height: 900px; }

  .card { position: absolute; left: 236px; width: 644px; overflow: hidden; }

  /* Front */
  .card--front { top: 30px; height: 394px; background: var(--card-dark); }
  .brand-mark { position: absolute; left: 0; top: 0; width: 644px; height: 394px; }
  .brand-name {
    position: absolute; left: 0; width: 644px; text-align: center;
    font-family: "Arimo", Arial, sans-serif; color: var(--on-dark);
  }
  .card--front .brand-name { top: 258px; font-size: 14px; }
  .brand-rule { position: absolute; height: 2px; background: var(--cyan); }
  .card--front .brand-rule { left: 208px; width: 218px; top: 278px; }
  .web-tab {
    position: absolute; font-family: "Arimo", Arial, sans-serif; font-size: 13px;
    line-height: 22px; height: 22px;
  }
  .web-tab--gold {
    left: 0; bottom: 0; width: 290px; padding-left: 6px;
    background: var(--gold); color: var(--ink); border-radius: 0 11px 11px 0;
  }

  /* Back */
  .card--back {
    top: 458px; height: 396px; background: var(--card-light);
    border: 1px solid var(--paper-edge);
  }
  .card--back .brand-name {
    left: 462px; width: 200px; top: 100px; font-size: 10px; color: var(--ink); text-align: left; padding-left: 6px;
  }
  .card--back .brand-rule { left: 464px; width: 138px; top: 114px; height: 1px; }

  .holder {
    position: absolute; right: 342px; top: 146px; text-align: right;
    font-family: "Tinos", "Times New Roman", serif;
  }
  .holder__name { font-size: 40px; color: var(--cyan); line-height: 46px; font-weight: 400; }
  .holder__title { font-size: 22px; color: var(--ink); line-height: 26px; }

  .divider { position: absolute; left: 303px; top: 126px; width: 2px; height: 210px; background: var(--ink); }

  .details {
    position: absolute; left: 311px; top: 220px; list-style: none;
    font-family: "Tinos", "Times New Roman", serif; font-size: 16px; line-height: 22px; color: var(--ink);
  }
  .details__label { color: var(--cyan); }

  .web-tab--dark {
    right: 0; bottom: 0; width: 294px; padding-left: 26px;
    background: var(--card-dark); color: var(--on-dark); border-radius: 11px 0 0 11px;
  }
</style>
</head>
<body>
<main class="canvas">

  <section class="card card--front" aria-label="Card front">
    <svg class="brand-mark" viewBox="0 0 644 394" aria-hidden="true">
      <circle cx="320" cy="164" r="76" fill="var(--gold)"/>
    </svg>
    <p class="brand-name">Brightline Electrical &amp; Refrigeration</p>
    <span class="brand-rule"></span>
    <p class="web-tab web-tab--gold">www.brightline-air.com.au</p>
  </section>

  <section class="card card--back" aria-label="Card back">
    <svg class="brand-mark" viewBox="0 0 644 396" aria-hidden="true">
      <circle cx="534" cy="52" r="46" fill="var(--card-dark)"/>
    </svg>
    <p class="brand-name">Brightline Electrical &amp; Refrigeration</p>
    <span class="brand-rule"></span>

    <div class="holder">
      <h1 class="holder__name">Peter Mulvane</h1>
      <p class="holder__title">Brightline</p>
    </div>

    <span class="divider"></span>

    <ul class="details">
      <li>Installation &amp; Decomissioning</li>
      <li>of aiconditioning split systems</li>
      <li><span class="details__label">LIC NO:</span> TKR 504613</li>
      <li><span class="details__label">Mobile no:</span> 0438 517 209</li>
      <li><span class="details__label">Email:</span> rtmulvane@kestrelnet.com.au</li>
    </ul>

    <p class="web-tab web-tab--dark">www.brightline-air.com.au</p>
  </section>

</main>
</body>
</html>
```